Wedding Marloes & Joost - Save the Date Wedding Card

I would like to have a creative save the date wedding card. We like grey/black/white colors and modern/ plain and simple.
I like the Save the Date copy big and book a flight copy smaller. I like stylish fonts for the save the date copy
Copy front:
Save the Date & book a flight
7-10-2017 Denia (Spanje)
Marloes & Joost
Onze dag is niet compleet zonder jou!
Copy back:
6-10 preferred travel date
7-10 wedding ceremony/drinks/dinner/party
8-10 hangover breakfast
Nearest Airports Valencia & Alicante
More info will be available soon!
Target Market(s)
wedding guests
Industry/Entity Type
Wedding

```html
<!DOCTYPE html>
<html lang="nl">
<head>
<meta charset="utf-8">
<title>Save the Date – Marloes &amp; Joost</title>
<link rel="stylesheet" href="https://fonts.googleapis.com/css2?family=Great+Vibes&family=Parisienne&display=swap">
<style>
  :root {
    --backdrop: #000000;
    --card: #e8e6e5;
    --card-edge: #7a7a7a;
    --rule: #d3d1d0;
    --ink: #111111;
    --ink-soft: #6a6a6a;
    --shadow: #9a9a9a;
  }
  html, body {
    margin: 0;
    padding: 0;
    width: 1200px;
    height: 1200px;
    overflow: hidden;
    background: var(--backdrop);
  }
  .canvas {
    position: relative;
    width: 1200px;
    height: 1200px;
  }
  .card {
    position: absolute;
    left: 88px;
    width: 1044px;
    height: 447px;
    box-sizing: border-box;
    border: 4px solid var(--card-edge);
    background-color: var(--card);
    background-image: repeating-linear-gradient(
      to bottom,
      transparent 0,
      transparent 18px,
      var(--rule) 18px,
      var(--rule) 20px
    );
    font-family: "Parisienne", cursive;
    color: var(--ink);
  }
  .card--front { top: 145px; }
  .card--back  { top: 648px; }

  .line {
    position: absolute;
    margin: 0;
    line-height: 1;
    white-space: nowrap;
    font-weight: 400;
  }
  .centered { left: 0; right: 0; text-align: center; }

  .headline { top: 22px; font-size: 62px; letter-spacing: 1px; }
  .date-place { top: 125px; font-size: 48px; }
  .couple {
    top: 190px;
    font-family: "Great Vibes", cursive;
    font-size: 140px;
    text-shadow: 4px 4px 0 var(--shadow);
    word-spacing: 12px;
  }
  .tagline { top: 398px; right: 20px; font-size: 27px; }

  .schedule {
    left: 20px;
    font-size: 52px;
    color: var(--ink-soft);
  }
  .schedule--travel { top: 35px; }
  .schedule--wedding { top: 115px; }
  .schedule--breakfast { top: 195px; }
  .airports { top: 335px; font-size: 36px; }
  .more-info { top: 398px; font-size: 23px; }
</style>
</head>
<body>
<main class="canvas">
  <section class="card card--front">
    <h1 class="line centered headline">Save The Date &amp; book a flight</h1>
    <p class="line centered date-place">7-10-2017 Denia Spanje</p>
    <p class="line centered couple">Marloes &amp; Joost</p>
    <p class="line tagline">Onze dag is niet compleet zonder jou!</p>
  </section>

  <section class="card card--back">
    <p class="line schedule schedule--travel">6-10 preferred travel date</p>
    <p class="line schedule schedule--wedding">7-10 wedding ceremony/drinks/dinner/party</p>
    <p class="line schedule schedule--breakfast">8-10 hangover breakfast</p>
    <p class="line centered airports">Nearest Airports Valencia &amp; Alicante</p>
    <p class="line centered more-info">More info will be available soon!</p>
  </section>
</main>
</body>
</html>
```